Mobile Repair Service on location needs a Web Design

We are starting a new mobile device repair service called Cell Revive and our website needs a design!

Hello Designers!
First, we'd like to make clear this is more than a simple web design contest, we want the designers to create an idea. We want someone who can create the whole theme of the service's we provide. We want someone that can help design our visual branding, help us communicate a sentiment. And we are willing to pay for that.

Who are we?
Our company is based in Rotterdam, the Netherlands. We provide different services for all kinds of electronic devices. The kind of services we provide are, among other things, installations of hardware and software and the repair of broken or malfunctioning devices.
We are starting a new service that offers mobile device repairs on location, be it at the home of our customers, their office, or any other place. Just give us the address and we will come to you for the repair job. This is also our main USP. We have multiple skilled engineers who drive trough the country on a daily basis and can be on location within a working day. Repair is done immediately onsite while the customer waits. At this stage we will start with the smartphone product-group within the mobile devices. In a second phase we might also add tablets.
People don't want to be without their phone for weeks because of some parts that needed to be ordered by a repair center they had to sent their phone to. We offer a fully functional mobile repair center in the form of specially customized vans. These vans have all the tools and utilities needed by our engineers to safely repair your mobile device. Your phone is being repaired directly in front of you, the next business-day, on a location you desire.

For this new service we are creating a website called Cell Revive. The website needs a story and matching design and this is where you come in. We are not looking for a simple template design we can get from any place. We need a story. We want you to create an idea, build a unique theme or vision that helps sell the product/service. This goes beyond the design of the website. We need the whole package, the design you are creating needs to have returning elements like icons, color use, images, maybe even characters etc. You name it! There needs to be a common thread in the design so we can reuse elements in, for example, the email templates, the work order or receipt we give to our customers (we may contact the winner of the contest to design these for us as well!).

The name 'Cell Revive' is chosen. Revive (short for rehabilitate) has a bold and playful tone to it and the design needs to reflect the name. So we're looking for a somewhat playful and cheeky design. Definitely not too serious and definitely modern. We already got a logo that we love and that fit's this description (see attached design documents for the logo). It's bold, powerful and fun. Our web design needs to reflect this as well and has to fit in with our logo.
We would really like it if the design somehow incorporates elements that highlight our unique selling points (repairs on location, we come to you etc.). We would really like some form of story telling in the design. Think clumsy people breaking their phones. Teenagers in tears because they have no access to their friends. People nowadays have the need to always be 'connected'. What happens when your phone is broken or malfunctioning? We're handling tech, we are nerds and a little bit weird, but we're professionals and here to help you with your problem. The sentiment Byte Troop tries to communicate is something we really like. We're looking for fresh idea's, anything goes!

In an overview all Unique Selling Points of the Cell revive service:
- Professional service on location. Don’t ship to us we will come to you!
- Clear pricing upfront. No hidden cost.
- Next business-day repair.
- Backed by a professional call center open 12 hours a day and open on a Saturday as well
- Backed by a professional repair center with more then 12 years of experience
- Repair is done by certified engineers
- 1 year warranty on the repair

The process:
The main function of our website will be for customers to make a repair request. A customer will visit our website and can make a repair request immediately by going through a 'request-order-flow'. In this flow he or she will need to fill in some forms and can select wich type/model/brand of mobile device he or she has and what parts need to be repaired. After a request is placed we will call the customer back (within an hour) for a short intake and to set a date/time and location. Our engineer will meet the customer at the specified location and will repair the device onsite in one of our mobile repair centers, which is a specialized van equipped with all the tools needed for device restorations.
So in short the steps are:
- Choose your device and repair job
- Place the order
- Get a callback within the hour
- Set date and location
- We will come to you.

Website functionality:
Our website is our main form of communication. So the sentiment we want to communicate needs be reflected in the design. We need a main/front page designed (preferably a long scrolling page design) containing:
1. Customers will be able to request a repair job directly on our website. So there will need to be a prominent button/link at the top of our main page that will bring the customer to this 'request-order-flow'. This is the main flow which needs to be full focus on the front page. All other items are secondary.
2. The general information of who we are and what we do, and why the customer should choose us. Preferably in short bullet-point type keywords/sentences with icons or other visual cues. See our unique selling points to get an idea of the information that will be displayed here.
3. There needs to be a section that will explain the process (see above) of a repair request step-by- step, again in brief short key sentences and with (custom) icons.
4. There needs to be a section that explains to the customer he/she can always contact us if they are not sure what the problem is with their device, and for this reason are not sure what repair request they should order.
5. We want to implement some functionality that display customer ratings or customer reviews. So there needs to be room for some kind of widget of plugin we're going to implement which shows these reviews.
6. A 'For business section' where we will explain all the options we provide for corporate clients.
7. Social media links.
8. There needs to be a menu with buttons that leads to the all sections described in the previous points.

For now, we need a design for our front page. In the second phase, when we have picked our winner, we may ask the winner to design the page(s) for our request workflow as well.

EDIT:
Finally, we have a very specific order in mind for the different segments of our website. We would like you to add some more segments that were not in our original brief as well:

1. Top header with order/request button. (should instantly make clear our main USP, we do repairs on location)
2. Our process
3. Our unique selling points / why choose us
4. The kind of repairs we do (broken screens, broken batteries, water damage, broken camera's, no sound etc.)
5. A 'meet our team' section, where we introduce some of our engineers
6. A 'contact us for any questions' section/
7. Testimonials/user reviews
8. A section where we show key performance indicators
9. 'For businesses' sections
10.'Subscribe for newsletter' field
11. Social media buttons
Updates

Industry/Entity Type

It Service

Number of Pages Required

1 page

Font styles to use
Sans Serif

Requirements
Must have
• a main/front page, design only
• custom icons/images for banners, adverts online and in print (high res)
Nice to have
• Storytelling in our design.
• Design that fits with our brand new logo.
• Elements like icons to have a flat design.
• Keep in mind that the website will need to be responsive when designing! (Ideally provide an example of the mobile design as well)
• Create a fun and trustworthy feeling.

```html
<!DOCTYPE html>
<html lang="en">
<head>
<meta charset="utf-8">
<title>Cell Revive – Mobile repair on location</title>
<link href="https://fonts.googleapis.com/css2?family=Montserrat:wght@300;400;500;600;700&family=Noto+Serif:ital@1&family=Roboto:wght@400;500&display=swap" rel="stylesheet">
<style>
:root{
  --orange:#ff8a00;
  --orange-soft:#ffd9a8;
  --ink:#111111;
  --text:#333333;
  --muted:#666666;
  --sky:#e3f4f8;
  --night:#161616;
  --blue:#1e8ff5;
  --link:#2f8ff0;
  --green:#2bb51e;
  --star:#4d9a6b;
  --line:#e3e3e3;
  --footer:#1c1c1c;
  --white:#ffffff;
}
*{margin:0;padding:0;box-sizing:border-box}
html,body{width:1200px;height:2908px;overflow:hidden}
body{position:relative;background:var(--white);font-family:"Montserrat",Arial,sans-serif;color:var(--text)}
.abs{position:absolute}

/* header */
.brand{left:128px;top:38px;display:flex;align-items:center;gap:14px}
.brand-dot{width:56px;height:56px;border-radius:50%;background:var(--orange)}
.brand-name{font-weight:700;font-size:28px;color:var(--ink);line-height:1}
.nav{font-size:12.5px;font-weight:500;color:var(--ink)}
.nav a{color:inherit;text-decoration:none;position:absolute;white-space:nowrap}

/* hero */
.hero-title{left:124px;top:182px;font-size:27px;font-weight:600;color:var(--ink);letter-spacing:.3px}
.hero-sub{left:148px;top:220px;font-size:20px;font-weight:300;color:var(--text)}
.door-ring{left:254px;top:264px;width:182px;height:182px;border-radius:50%;background:var(--orange-soft)}
.door-core{left:273px;top:283px;width:144px;height:144px;border-radius:50%;background:var(--orange)}
.door-core svg{position:absolute;left:42px;top:40px}
.doorstep{left:195px;top:458px;width:300px;text-align:center;font-size:22px;font-weight:300;color:var(--text);line-height:1.3;letter-spacing:.5px}
.quickest{left:160px;top:522px;width:370px;text-align:center;font-size:16px;color:var(--text)}
.btn-request{left:223px;top:574px;width:244px;height:62px;background:var(--orange);color:var(--white);font-weight:700;font-size:18px;display:flex;align-items:center;justify-content:center;letter-spacing:.3px}
.hero-art{left:540px;top:290px;width:610px;height:310px;border-radius:40px 40px 60px 60px;background:radial-gradient(ellipse at 50% 55%,#2a2a2a 0%,#555 45%,#cfcfcf 75%,#ffffff 100%);transform:rotate(-14deg)}

/* why */
.why{left:0;top:675px;width:1200px;height:675px;background:var(--sky)}
.why-title{left:0;top:712px;width:1200px;text-align:center;font-size:31px;font-weight:300;color:var(--ink)}
.why-title b{color:var(--orange);font-weight:700}
.usp{width:300px}
.usp h3{font-size:17px;font-weight:600;color:var(--ink);line-height:1.3;letter-spacing:.3px}
.usp p{font-size:17px;color:var(--text);line-height:1.35;margin-top:3px}
.usp-icon{width:70px;height:70px}

/* how it works */
.how{left:0;top:1350px;width:1200px;height:674px;background:var(--night)}
.how-title{left:0;top:1463px;width:1200px;text-align:center;font-size:31px;font-weight:300;color:var(--white);line-height:1.25}
.how-title b{display:block;color:var(--green);font-weight:700}
.step-icon{width:84px;height:84px}
.step-dot{width:20px;height:20px;border-radius:50%;border:3px solid var(--link)}
.step-line{height:2px;background:var(--link)}
.step-line::after{content:"";position:absolute;right:-2px;top:-5px;border-left:9px solid var(--link);border-top:6px solid transparent;border-bottom:6px solid transparent}
.step{width:200px;text-align:center;color:var(--link)}
.step h4{font-size:17px;font-weight:700;line-height:1.25}
.step p{font-size:17px;line-height:1.3;margin-top:2px}

/* call to action band */
.cta{left:0;top:2024px;width:1200px;height:159px;background:var(--blue)}
.cta-head{left:124px;top:2063px;font-size:18px;font-weight:700;color:var(--white)}
.cta-text{left:124px;top:2088px;width:420px;font-size:18px;color:var(--white);line-height:1.3}
.btn-cta{left:830px;top:2071px;width:244px;height:66px;background:var(--white);color:var(--blue);font-weight:700;font-size:18px;display:flex;align-items:center;justify-content:center}

/* reviews */
.rev-kicker{left:0;top:2252px;width:1200px;text-align:center;font-family:"Noto Serif",Georgia,serif;font-style:italic;font-size:18px;color:var(--ink)}
.rev-title{left:0;top:2278px;width:1200px;text-align:center;font-family:"Roboto",Arial,sans-serif;font-size:32px;font-weight:500;color:var(--ink)}
.rev-rule{top:2288px;height:1px;background:var(--line)}
.summary{left:74px;top:2346px;width:236px;height:181px;border:1px solid var(--line);text-align:center;font-family:"Roboto",Arial,sans-serif;background:var(--white)}
.summary h5{font-size:21px;font-weight:500;color:var(--ink);margin-top:18px}
.stars{color:var(--star);letter-spacing:4px;font-size:17px}
.summary .stars{margin-top:10px}
.summary .based{font-family:"Noto Serif",Georgia,serif;font-style:italic;font-size:13px;color:var(--text);margin-top:6px}
.see-all{position:absolute;left:50px;top:124px;font-size:13px;font-weight:500;color:var(--star);display:flex;align-items:center;gap:10px}
.see-all span{width:34px;height:34px;border-radius:50%;border:1px solid var(--line);display:flex;align-items:center;justify-content:center;color:var(--text)}
.review{width:220px;font-family:"Roboto",Arial,sans-serif}
.review .stars{font-size:15px;letter-spacing:3px}
.review h6{font-size:21px;font-weight:500;color:var(--ink);line-height:1.2;margin-top:10px}
.review q{display:block;width:185px;font-family:"Noto Serif",Georgia,serif;font-style:italic;font-size:13px;color:var(--text);line-height:1.5;margin-top:8px;quotes:"\201C" "\201D"}
.review .who{position:absolute;top:161px;font-size:12px;font-weight:500;color:var(--star)}
.review .when{position:absolute;top:178px;font-size:10px;color:#999}
.rev-base{left:0;top:2604px;width:1200px;height:1px;background:var(--line)}
.arrow-btn{top:2583px;width:42px;height:42px;border-radius:50%;border:2px solid var(--star);background:var(--white);display:flex;align-items:center;justify-content:center;color:var(--ink);font-size:16px;font-family:"Roboto",Arial,sans-serif}

/* footer */
.footer{left:0;top:2705px;width:1200px;height:203px;background:var(--footer)}
.contact-head{left:124px;top:2736px;font-size:18px;font-weight:700;color:var(--white)}
.contact-line{left:124px;font-size:18px;color:var(--white)}
.follow{left:727px;top:2736px;font-size:18px;color:var(--white)}
.social{top:2794px;font-size:15px;font-weight:600;color:var(--white);white-space:nowrap;transform:translateX(-50%)}
</style>
</head>
<body>

<!-- header -->
<div class="abs brand">
  <div class="brand-dot"></div>
  <div class="brand-name">Cell Revive</div>
</div>
<nav class="abs nav" style="left:0;top:57px;width:1200px">
  <a style="left:506px">WHY CELL REVIVE</a>
  <a style="left:698px">HOW IT WORKS</a>
  <a style="left:839px">CUSTOMER REVIEWS</a>
  <a style="left:1010px">CONTACT</a>
</nav>

<!-- hero -->
<h1 class="abs hero-title">BROKEN PHONE OR TABLET?</h1>
<p class="abs hero-sub">We are the solution to your problems</p>
<div class="abs door-ring"></div>
<div class="abs door-core">
  <svg width="60" height="66" viewBox="0 0 60 66"><rect x="8" y="2" width="44" height="62" fill="none" stroke="#fff" stroke-width="4"/><path d="M8 2 L36 8 L36 64 L8 64 Z" fill="#fff"/><circle cx="31" cy="36" r="2.5" fill="#ff8a00"/></svg>
</div>
<p class="abs doorstep">WE COME TO YOUR<br>DOORSTEP</p>
<p class="abs quickest">The quickest way to repair your device</p>
<div class="abs btn-request">REQUEST A REPAIR</div>
<div class="abs hero-art" role="img" aria-label="Smartphone with a shattered screen, glass shards flying off"></div>

<!-- why -->
<section class="abs why"></section>
<h2 class="abs why-title">WHY <b>CELL REVIVE?</b></h2>

<svg class="abs usp-icon" style="left:152px;top:838px" viewBox="0 0 70 70"><path d="M4 30 L22 20 L34 28 L48 20 L66 30 L56 46 L40 54 L26 50 L14 42 Z" fill="#1e8ff5"/><path d="M26 36 L38 46 M32 32 L44 42" stroke="#0b5cb0" stroke-width="3"/></svg>
<div class="abs usp" style="left:252px;top:846px"><h3>PROFESSIONAL SERVICE<br>ON LOCATION.</h3><p>Don't ship to us we will<br>come to you!</p></div>

<svg class="abs usp-icon" style="left:645px;top:846px" viewBox="0 0 70 70"><rect x="10" y="6" width="50" height="60" rx="10" fill="#1e8ff5"/><rect x="18" y="14" width="34" height="30" rx="4" fill="#e3f4f8"/><rect x="26" y="50" width="18" height="6" rx="3" fill="#e3f4f8"/></svg>
<div class="abs usp" style="left:727px;top:846px"><h3>12 HOUR CALL CENTER</h3><p>Backed by a professional call center open 12 hours a day and open on a Saturday as well</p></div>

<svg class="abs usp-icon" style="left:152px;top:1004px" viewBox="0 0 70 70"><circle cx="35" cy="35" r="32" fill="#1e8ff5"/><text x="35" y="49" text-anchor="middle" font-family="Montserrat,sans-serif" font-weight="700" font-size="38" fill="#fff">$</text></svg>
<div class="abs usp" style="left:252px;top:1012px"><h3>CLEAR PRICING<br>UPFRONT.</h3><p>No hidden cost.</p></div>

<svg class="abs usp-icon" style="left:645px;top:1004px" viewBox="0 0 70 70"><circle cx="35" cy="26" r="20" fill="#1e8ff5"/><circle cx="35" cy="26" r="11" fill="#e3f4f8"/><circle cx="35" cy="26" r="6" fill="#1e8ff5"/><path d="M22 42 L16 66 L26 60 L30 68 L35 46 Z M48 42 L54 66 L44 60 L40 68 L35 46 Z" fill="#1e8ff5"/></svg>
<div class="abs usp" style="left:727px;top:1012px"><h3>REPAIR IS DONE BY CERTIFIED<br>ENGINEERS</h3><p>Backed by a professional repair center with more then 12 years of experience.</p></div>

<svg class="abs usp-icon" style="left:148px;top:1168px;width:82px" viewBox="0 0 82 70"><circle cx="18" cy="16" r="13" fill="#e3f4f8" stroke="#1b3b6b" stroke-width="3"/><path d="M18 9 V16 H24" stroke="#1b3b6b" stroke-width="3" fill="none"/><path d="M20 30 H56 V58 H20 Z M56 38 H68 L76 48 V58 H56 Z" fill="#1e8ff5" stroke="#1b3b6b" stroke-width="3"/><circle cx="30" cy="60" r="6" fill="#e3f4f8" stroke="#1b3b6b" stroke-width="3"/><circle cx="64" cy="60" r="6" fill="#e3f4f8" stroke="#1b3b6b" stroke-width="3"/></svg>
<div class="abs usp" style="left:252px;top:1178px"><h3>NEXT BUSINESS-DAY<br>REPAIR.</h3></div>

<svg class="abs usp-icon" style="left:645px;top:1168px" viewBox="0 0 70 70"><rect x="18" y="4" width="36" height="62" rx="3" fill="#1e8ff5"/><rect x="22" y="12" width="28" height="44" fill="#e3f4f8"/><path d="M28 44 V34 H32 L38 24 C41 24 41 28 40 32 H46 V44 Z" fill="#1e8ff5"/></svg>
<div class="abs usp" style="left:727px;top:1178px"><h3>1 YEAR WARRANTY ON THE<br>REPAIR.</h3><p>We offer lightening fast turnarounds. No hassle, Guaranteed!</p></div>

<!-- how it works -->
<section class="abs how"></section>
<h2 class="abs how-title">HOW IT WORKS.<b>WE COME TO YOU</b></h2>

<svg class="abs step-icon" style="left:181px;top:1660px" viewBox="0 0 84 84"><rect x="26" y="10" width="32" height="62" rx="4" fill="none" stroke="#2f8ff0" stroke-width="3"/><line x1="36" y1="17" x2="48" y2="17" stroke="#2f8ff0" stroke-width="3"/><path d="M34 50 L50 32 M38 54 L46 44" stroke="#2f8ff0" stroke-width="2"/><circle cx="42" cy="65" r="2.5" fill="#2f8ff0"/></svg>
<svg class="abs step-icon" style="left:439px;top:1660px" viewBox="0 0 84 84"><circle cx="18" cy="18" r="11" fill="none" stroke="#2bb51e" stroke-width="3"/><path d="M13 18 L17 22 L24 14" stroke="#2bb51e" stroke-width="3" fill="none"/><path d="M14 36 H54 V62 H14 Z M54 44 H66 L76 54 V62 H54 Z" fill="#1e8ff5"/><circle cx="26" cy="64" r="6" fill="#161616" stroke="#fff" stroke-width="3"/><circle cx="64" cy="64" r="6" fill="#161616" stroke="#fff" stroke-width="3"/></svg>
<svg class="abs step-icon" style="left:699px;top:1660px" viewBox="0 0 84 84"><rect x="10" y="16" width="52" height="50" rx="6" fill="none" stroke="#2f8ff0" stroke-width="3"/><line x1="10" y1="28" x2="62" y2="28" stroke="#2f8ff0" stroke-width="3"/><path d="M20 10 V22 M30 10 V22 M42 10 V22 M52 10 V22" stroke="#2f8ff0" stroke-width="3"/><text x="34" y="56" text-anchor="middle" font-family="Montserrat,sans-serif" font-weight="700" font-size="22" fill="#2f8ff0">23</text><circle cx="62" cy="62" r="13" fill="#161616" stroke="#2bb51e" stroke-width="3"/><path d="M55 62 L60 67 L69 57" stroke="#2bb51e" stroke-width="3" fill="none"/></svg>
<svg class="abs step-icon" style="left:958px;top:1652px" viewBox="0 0 84 84"><rect x="28" y="22" width="28" height="48" rx="3" fill="none" stroke="#2f8ff0" stroke-width="3"/><path d="M35 46 L40 51 L49 40" stroke="#2bb51e" stroke-width="3" fill="none"/><path d="M64 8 V18 M59 13 H69 M70 24 V30 M67 27 H73 M14 36 V44 M10 40 H18" stroke="#2bb51e" stroke-width="2"/></svg>

<div class="abs step-dot" style="left:213px;top:1780px"></div>
<div class="abs step-line" style="left:247px;top:1789px;width:208px"></div>
<div class="abs step-dot" style="left:471px;top:1780px"></div>
<div class="abs step-line" style="left:505px;top:1789px;width:210px"></div>
<div class="abs step-dot" style="left:731px;top:1780px"></div>
<div class="abs step-line" style="left:765px;top:1789px;width:209px"></div>
<div class="abs step-dot" style="left:990px;top:1780px"></div>

<div class="abs step" style="left:123px;top:1834px"><h4>TELL US THE<br>PROBLEM.</h4><p>Choose your device and repair job.</p></div>
<div class="abs step" style="left:381px;top:1834px"><h4>PLACE THE ORDER.</h4><p>Get a callback within the hour.</p></div>
<div class="abs step" style="left:641px;top:1834px"><h4>SET DATE AND<br>LOCATION</h4><p>We recieve your order and confirm appointment.</p></div>
<div class="abs step" style="left:900px;top:1834px"><h4>WE FIX YOUR<br>DEVICE</h4><p>We will come to you and fix your device.</p></div>

<!-- call to action -->
<section class="abs cta"></section>
<p class="abs cta-head">DO YOU NEED A MOBILE PHONE REPAIR?</p>
<p class="abs cta-text">Choose your device and repair job. We will come to you.</p>
<div class="abs btn-cta">REQUEST A REPAIR</div>

<!-- reviews -->
<p class="abs rev-kicker">What our customers</p>
<h2 class="abs rev-title">Are Saying</h2>
<div class="abs rev-rule" style="left:0;width:490px"></div>
<div class="abs rev-rule" style="left:700px;width:500px"></div>

<div class="abs summary">
  <h5>Excellent</h5>
  <div class="stars">★★★★★</div>
  <p class="based">Based on 1,979 reviews</p>
  <div class="see-all">See all reviews <span>›</span></div>
</div>

<div class="abs review" style="left:361px;top:2350px">
  <div class="stars">★★★★☆</div>
  <h6>As good as<br>advertised</h6>
  <q>Great service at the right price</q>
  <span class="who">Mrs Anna Brooks</span><span class="when">44 Hours Ago</span>
</div>
<div class="abs review" style="left:609px;top:2350px">
  <div class="stars">★★★☆☆</div>
  <h6>Excellent service<br>and good quality</h6>
  <q>Placed my order. Arrived on time, fixed me up and I was good again.</q>
  <span class="who">Mrs Julia Marsh</span><span class="when">About 1 hour ago</span>
</div>
<div class="abs review" style="left:859px;top:2350px">
  <div class="stars">★★★★☆</div>
  <h6>Efficient and helful<br>in every way</h6>
  <q>Cried when my phone broke... but you guys saved me. Y'all were helpful and efficient</q>
  <span class="who">Mr Owen Fletcher</span><span class="when">4 days ago</span>
</div>

<div class="abs rev-base"></div>
<div class="abs arrow-btn" style="left:553px">‹</div>
<div class="abs arrow-btn" style="left:603px">›</div>

<!-- footer -->
<footer class="abs footer"></footer>
<p class="abs contact-head">CONTACT US</p>
<p class="abs contact-line" style="top:2771px">1-800-555-0142</p>
<p class="abs contact-line" style="top:2806px">88 Canal Street, Rotterdam</p>
<p class="abs contact-line" style="top:2841px">mail@cellrevive.com</p>
<p class="abs follow">Follow Us</p>
<span class="abs social" style="left:748px">Friendbook</span>
<span class="abs social" style="left:847px">Chirper</span>
<span class="abs social" style="left:944px">Circles+</span>
<span class="abs social" style="left:1045px">Snapgram</span>

</body>
</html>
```